I need a flyer designed for a marine service company. Our company specializes in boat engine diagnostic/repair, engine service, electronic installation and repairs, bottom paint, detailing, winterization and shrink wrapping. We would like to see designs that incorporate our color scheme of deep blue, blueish gray and black (please see attached photo)

Target Market(s)

Boat owners

Industry/Entity Type

Marine

Logo Text

Kelpridge Harbor Services

Requirements
Must have
• Company logo
Nice to have
• List the services we provide.

```html
<!DOCTYPE html>
<html lang="en">
<head>
<meta charset="utf-8">
<title>Kelpridge Harbor Services – Flyer</title>
<link rel="stylesheet" href="https://fonts.googleapis.com/css2?family=Montserrat:wght@400;500;600;700;800&display=swap">
<style>
  :root {
    --sky-top: #0a7bd9;
    --sky-mid: #4f9bd6;
    --sea: #2c5f92;
    --spray: #dfe9f1;
    --navy: #14264a;
    --deep-sea: #0b3a6a;
    --deep-sea-dark: #0a2547;
    --white: #ffffff;
    --ink: #1b2233;
    --page: #e9edf1;
  }
  * { margin: 0; padding: 0; box-sizing: border-box; }
  html, body { width: 1200px; height: 2234px; overflow: hidden; }
  body { background: var(--page); font-family: "Montserrat", sans-serif; position: relative; }

  .flyer { position: absolute; left: 0; top: 268px; width: 1200px; height: 1698px; overflow: hidden; background: var(--white); }
  .flyer-shapes { position: absolute; inset: 0; }

  .headline { position: absolute; left: 0; width: 1200px; top: 72px; text-align: center; color: var(--white); }
  .headline .line-one { font-size: 58px; font-weight: 400; line-height: 80px; }
  .headline .line-one strong { font-weight: 800; }
  .headline .line-two { font-size: 64px; font-weight: 800; line-height: 82px; }

  .brand { position: absolute; left: 127px; top: 667px; width: 330px; height: 330px; border-radius: 50%; background: var(--white);
           display: flex; flex-direction: column; align-items: center; justify-content: center; text-align: center;
           color: var(--navy); font-weight: 600; }
  .brand .brand-main { font-size: 40px; line-height: 46px; }
  .brand .brand-sub { font-size: 24px; line-height: 32px; letter-spacing: 1px; }

  .section-tab { position: absolute; left: 0; top: 979px; width: 1200px; height: 106px; }
  .section-title { position: absolute; left: 430px; top: 979px; width: 330px; height: 106px; line-height: 106px; text-align: center;
                   color: var(--white); font-size: 38px; font-weight: 700; }

  .services { position: absolute; top: 1112px; list-style: none; }
  .services.left { left: 88px; }
  .services.right { left: 643px; }
  .services li { display: flex; align-items: center; height: 47px; font-size: 26px; font-weight: 500; color: var(--ink); }
  .services svg { width: 20px; height: 20px; margin-right: 12px; flex: none; }

  .gallery { position: absolute; top: 1277px; left: 0; width: 1200px; height: 220px; }
  .gallery-item { position: absolute; top: 0; width: 220px; height: 220px; border-radius: 50%; border: 6px solid var(--white);
                  box-shadow: 0 0 0 2px var(--navy); }
  .gallery-item.boat-trailer { left: 105px; background: linear-gradient(180deg, #a9bccb 0%, #e4e8ec 45%, #4a5562 100%); }
  .gallery-item.parts-layout { left: 362px; background: radial-gradient(circle at 50% 50%, #3b4148 0%, #c9d6da 40%, #e7ecee 100%); }
  .gallery-item.carburetor { left: 618px; background: radial-gradient(circle at 50% 45%, #7b5532 0%, #b59a80 45%, #a5a8ab 100%); }
  .gallery-item.shrink-wrap { left: 875px; background: linear-gradient(180deg, #6e7560 0%, #dde2e6 45%, #e9ecef 70%, #5d636a 100%); }

  .contact-email { position: absolute; left: 82px; top: 1610px; display: flex; align-items: center; color: var(--white);
                   font-size: 32px; font-weight: 500; }
  .contact-email svg { width: 26px; height: 20px; margin-right: 14px; }
  .contact-phone { position: absolute; left: 743px; top: 1595px; width: 457px; height: 70px; border-radius: 35px 0 0 35px;
                   background: var(--navy); display: flex; align-items: center; padding-left: 14px; color: var(--white);
                   font-size: 25px; font-weight: 500; }
  .contact-phone svg { width: 38px; height: 38px; margin-right: 10px; }
</style>
</head>
<body>
<main class="flyer">
  <svg class="flyer-shapes" width="1200" height="1698" viewBox="0 0 1200 1698">
    <defs>
      <linearGradient id="heroGradient" x1="0" y1="0" x2="0" y2="1">
        <stop offset="0" stop-color="var(--sky-top)"/>
        <stop offset="0.42" stop-color="var(--sky-mid)"/>
        <stop offset="0.62" stop-color="var(--sea)"/>
        <stop offset="0.85" stop-color="var(--spray)"/>
      </linearGradient>
      <linearGradient id="seaGradient" x1="0" y1="0" x2="0" y2="1">
        <stop offset="0" stop-color="var(--deep-sea)"/>
        <stop offset="1" stop-color="var(--deep-sea-dark)"/>
      </linearGradient>
    </defs>
    <rect class="hero-photo" x="0" y="0" width="1200" height="980" fill="url(#heroGradient)" role="img" aria-label="Photo of a white motor yacht speeding across blue water with green hills behind"/>
    <path class="content-panel" d="M0,965 C300,905 700,915 1200,790 L1200,1698 L0,1698 Z" fill="var(--white)"/>
    <path class="wave-band" d="M420,785 C600,830 800,900 1000,870 C1100,855 1170,830 1200,795 L1200,835 C1130,925 1000,965 850,960 C700,955 560,905 420,862 Z" fill="var(--navy)"/>
    <path class="wave-line" d="M420,880 C560,930 720,975 880,985" stroke="var(--navy)" stroke-width="6" fill="none"/>
    <path class="wave-line" d="M0,940 C40,900 90,870 150,850" stroke="var(--navy)" stroke-width="10" fill="none"/>
    <path class="wave-line" d="M40,955 C80,925 120,905 160,895" stroke="var(--navy)" stroke-width="4" fill="none"/>
    <path class="sea-photo" d="M0,1362 C150,1410 300,1440 450,1420 C650,1395 800,1320 1000,1330 C1100,1335 1170,1350 1200,1360 L1200,1698 L0,1698 Z" fill="url(#seaGradient)" role="img" aria-label="Photo of deep blue rippling sea water"/>
    <polygon class="section-tab" points="440,979 778,979 752,1085 410,1085" fill="var(--navy)"/>
  </svg>

  <header class="headline">
    <p class="line-one">Our company <strong>Specializes</strong> in</p>
    <p class="line-two">Boat Engine Diagnostic</p>
  </header>

  <div class="brand">
    <span class="brand-main">Kelpridge</span>
    <span class="brand-sub">HARBOR SERVICES</span>
  </div>

  <h2 class="section-title">What We Do</h2>

  <ul class="services left">
    <li><svg viewBox="0 0 20 20"><circle cx="10" cy="10" r="8" fill="none" stroke="var(--ink)" stroke-width="1.6"/><path d="M6,10.5 L9,13 L14,7.5" fill="none" stroke="var(--ink)" stroke-width="1.6"/></svg>Repair</li>
    <li><svg viewBox="0 0 20 20"><circle cx="10" cy="10" r="8" fill="none" stroke="var(--ink)" stroke-width="1.6"/><path d="M6,10.5 L9,13 L14,7.5" fill="none" stroke="var(--ink)" stroke-width="1.6"/></svg>Engine Service</li>
    <li><svg viewBox="0 0 20 20"><circle cx="10" cy="10" r="8" fill="none" stroke="var(--ink)" stroke-width="1.6"/><path d="M6,10.5 L9,13 L14,7.5" fill="none" stroke="var(--ink)" stroke-width="1.6"/></svg>Electronic Installation and Repairs</li>
  </ul>
  <ul class="services right">
    <li><svg viewBox="0 0 20 20"><circle cx="10" cy="10" r="8" fill="none" stroke="var(--ink)" stroke-width="1.6"/><path d="M6,10.5 L9,13 L14,7.5" fill="none" stroke="var(--ink)" stroke-width="1.6"/></svg>Bottom Paint</li>
    <li><svg viewBox="0 0 20 20"><circle cx="10" cy="10" r="8" fill="none" stroke="var(--ink)" stroke-width="1.6"/><path d="M6,10.5 L9,13 L14,7.5" fill="none" stroke="var(--ink)" stroke-width="1.6"/></svg>Detailing</li>
    <li><svg viewBox="0 0 20 20"><circle cx="10" cy="10" r="8" fill="none" stroke="var(--ink)" stroke-width="1.6"/><path d="M6,10.5 L9,13 L14,7.5" fill="none" stroke="var(--ink)" stroke-width="1.6"/></svg>Winterization and Shrink Wrapping</li>
  </ul>

  <div class="gallery">
    <div class="gallery-item boat-trailer" role="img" aria-label="Photo of a white bowrider boat on a trailer"></div>
    <div class="gallery-item parts-layout" role="img" aria-label="Photo of disassembled engine parts laid out on a table"></div>
    <div class="gallery-item carburetor" role="img" aria-label="Photo of an opened carburetor being serviced"></div>
    <div class="gallery-item shrink-wrap" role="img" aria-label="Photo of a boat covered in white shrink wrap"></div>
  </div>

  <p class="contact-email"><svg viewBox="0 0 26 20"><rect x="1" y="1" width="24" height="18" fill="var(--white)"/><path d="M1,1 L13,11 L25,1" fill="none" stroke="var(--navy)" stroke-width="2"/></svg>hello@kelpridgeharbor.com</p>
  <p class="contact-phone"><svg viewBox="0 0 38 38"><circle cx="19" cy="19" r="16" fill="none" stroke="var(--white)" stroke-width="2"/><path d="M13,11 L16,11 L17.5,15 L15.5,16.5 C16.5,19 18.5,21 21,22 L22.5,20 L26.5,21.5 L26.5,24.5 C26.5,26 25,27 23.5,26.8 C17,26 12,21 11.2,14.5 C11,12.5 12,11 13,11 Z" fill="var(--white)"/></svg>Call Us Today: +1 555-014-3382</p>
</main>
</body>
</html>
```